Need a stunning looking Business Card Design for my Telecom Business, Wow FACTOR!

I deal with high level IT Directors , and Contractors.
I need to impress them with a sleek , professional and unique business card.
Im thinking options as far as rounded edges, plastic , or even metal card or die cut on a corner.
Whatever looks better and leave an unforgettable first impression.
im looking for the wow factor.
Front should have the basics info (attached on the picture of current business card)
i would like to add picture of myself somewhere
Back side
should have logo and maybe some pictures or past projects, you can download from my website ( www.brivelgroup.com)

```html
<!DOCTYPE html>
<html lang="en">
<head>
<meta charset="utf-8">
<title>Brivel Technologies – Business Card</title>
<link rel="stylesheet" href="https://fonts.googleapis.com/css2?family=Lato:wght@400;700&display=swap">
<style>
  :root {
    --backdrop: #a7a7a7;
    --paper: #ffffff;
    --navy: #1b2452;
    --navy-deep: #16204a;
    --brand-blue: #2a86c9;
    --sky: #4fb3e6;
    --accent-red: #d3202a;
    --accent-orange: #f28c1c;
    --accent-green: #5a9e2f;
    --ink-gray: #6b6b6b;
  }
  * { margin: 0; padding: 0; box-sizing: border-box; }
  html, body {
    width: 1200px; height: 929px; overflow: hidden;
    background: var(--backdrop);
    font-family: "Lato", Arial, sans-serif;
  }
  .canvas { position: relative; width: 1200px; height: 929px; }

  .card {
    position: absolute;
    width: 620px; height: 354px;
    border-radius: 28px;
    overflow: hidden;
    box-shadow: 0 14px 30px rgba(0,0,0,0.28);
  }

  /* Front */
  .card-front { left: 60px; top: 70px; background: var(--paper); }
  .front-waves { position: absolute; inset: 0; width: 100%; height: 100%; }
  .contact-block { position: absolute; left: 44px; top: 50px; }
  .person-name {
    font-size: 24px; color: var(--accent-green); font-weight: 400;
    letter-spacing: 0.5px; text-transform: uppercase;
  }
  .person-name strong { font-weight: 700; }
  .person-role { font-size: 16px; color: var(--ink-gray); margin-top: 2px; }
  .person-tagline { font-size: 14px; color: var(--ink-gray); margin-top: 14px; line-height: 1.3; }
  .contact-list { list-style: none; margin-top: 26px; font-size: 15px; color: var(--ink-gray); }
  .contact-row { display: flex; align-items: flex-start; gap: 10px; margin-bottom: 10px; line-height: 1.3; }
  .contact-icon { width: 14px; height: 14px; flex: none; margin-top: 3px; }
  .brand-lockup {
    position: absolute; right: 44px; top: 70px;
    display: flex; align-items: center; gap: 12px;
    color: var(--navy); font-weight: 700; text-transform: uppercase;
  }
  .brand-dot { width: 22px; height: 22px; border-radius: 50%; background: var(--brand-blue); flex: none; }
  .brand-name { font-size: 30px; letter-spacing: 1px; line-height: 1; }
  .brand-name span { display: block; font-size: 12px; letter-spacing: 6px; margin-top: 6px; }
  .front-web {
    position: absolute; right: 40px; top: 272px;
    color: #ffffff; font-size: 15px; letter-spacing: 0.5px;
  }

  /* Back */
  .card-back { left: 520px; top: 505px; background: var(--navy-deep); }
  .back-lockup {
    position: absolute; left: 0; right: 0; top: 0; bottom: 0;
    display: flex; align-items: center; justify-content: center; gap: 16px;
    color: var(--sky); font-weight: 700; text-transform: uppercase;
  }
  .back-lockup .brand-dot { background: var(--sky); width: 28px; height: 28px; }
  .back-lockup .brand-name { font-size: 40px; }
  .back-lockup .brand-name span { font-size: 15px; letter-spacing: 9px; }
</style>
</head>
<body>
<main class="canvas">

  <section class="card card-front" aria-label="Business card front">
    <svg class="front-waves" viewBox="0 0 620 354" preserveAspectRatio="none" aria-hidden="true">
      <path d="M0 354 L0 342 C180 336 380 268 620 218 L620 354 Z" fill="var(--navy)"/>
      <path d="M150 330 C300 300 440 236 620 198" fill="none" stroke="var(--accent-red)" stroke-width="6"/>
      <path d="M0 326 C110 324 190 316 250 298" fill="none" stroke="var(--accent-orange)" stroke-width="7"/>
      <path d="M0 346 C160 344 260 330 350 300" fill="none" stroke="var(--sky)" stroke-width="4"/>
    </svg>

    <div class="contact-block">
      <h1 class="person-name"><strong>Dean</strong> Morimoto</h1>
      <p class="person-role">Operations Manager</p>
      <p class="person-tagline">Low Voltage Contractor Offices<br>in Miami, Broward and Palm Beach</p>
      <ul class="contact-list">
        <li class="contact-row">
          <svg class="contact-icon" viewBox="0 0 24 24" aria-hidden="true"><path fill="var(--accent-red)" d="M6.6 10.8a15.1 15.1 0 0 0 6.6 6.6l2.2-2.2a1 1 0 0 1 1-.25 11.4 11.4 0 0 0 3.6.57 1 1 0 0 1 1 1V20a1 1 0 0 1-1 1A17 17 0 0 1 3 4a1 1 0 0 1 1-1h3.5a1 1 0 0 1 1 1c0 1.25.2 2.45.57 3.57a1 1 0 0 1-.25 1z"/></svg>
          <span>(305) 555 0142 Miami<br>(954) 555 0178 Broward<br>(561) 555 0193 Palm Beach</span>
        </li>
        <li class="contact-row">
          <svg class="contact-icon" viewBox="0 0 24 24" aria-hidden="true"><rect x="2" y="5" width="20" height="14" rx="2" fill="var(--accent-green)"/><path d="M3 6 L12 13 L21 6" fill="none" stroke="#fff" stroke-width="2"/></svg>
          <span>info@brivelgroup.com</span>
        </li>
      </ul>
    </div>

    <div class="brand-lockup">
      <span class="brand-dot"></span>
      <p class="brand-name">Brivel<span>Technologies</span></p>
    </div>

    <p class="front-web">www.brivelgroup.com</p>
  </section>

  <section class="card card-back" aria-label="Business card back">
    <div class="back-lockup">
      <span class="brand-dot"></span>
      <p class="brand-name">Brivel<span>Technologies</span></p>
    </div>
  </section>

</main>
</body>
</html>
```